Landing page for 'Page under construction' page

We need a simple landing page that we can use while our page is under construction.

The page should be made ready so that all we need to do is drop it on our web server and then it will function as our webpage. The domain is www.tlv-demo.no

Please see attached file for instructions on what elements to include in the landing page. The Brand Book provides fonts and color palette.

Coding

Coded - Design and coding required

Number of Pages Required

1 page

Colors

Designer to choose colors to be used in the design.

```html
<!DOCTYPE html>
<html lang="en">
<head>
<meta charset="utf-8">
<title>Tellvik – Page is Under Construction</title>
<link rel="stylesheet" href="https://fonts.googleapis.com/css2?family=Montserrat:wght@600;700&family=Lato:wght@400;700&family=Roboto:wght@400;500;700&display=swap">
<style>
:root{
  --navy:#0c3468;
  --navy-deep:#0a3a78;
  --blue:#2a88c8;
  --sky:#4ea3d6;
  --orange:#f0954a;
  --coral:#ea5a58;
  --ink:#1a1a1a;
  --grey:#555b63;
  --paper:#eeeef0;
  --white:#ffffff;
}
*{margin:0;padding:0;box-sizing:border-box}
html,body{width:696px;height:1200px;overflow:hidden}
body{position:relative;font-family:"Lato",sans-serif;color:var(--ink);background:var(--white)}
.abs{position:absolute}
.brand{font-family:"Montserrat",sans-serif;font-weight:700;color:var(--navy);font-size:24px;letter-spacing:.3px;display:flex;align-items:center;gap:6px}
.brand .dot{width:8px;height:8px;background:var(--orange);border-radius:50%}

/* hero */
.hero{left:0;top:0;width:696px;height:350px;background:linear-gradient(170deg,#3a6ea8 0%,#3f86c2 45%,#56a8da 100%);overflow:hidden}
.hero .brand{left:65px;top:22px;color:var(--navy)}
.hero-mail{left:452px;top:26px;display:flex;align-items:center;gap:12px;color:var(--white);font-size:8.5px}
.hero-mail .ring{width:18px;height:18px;border:1.2px solid var(--white);border-radius:50%;display:flex;align-items:center;justify-content:center}
.lang{left:601px;top:30px;color:var(--white);font-size:8.5px;font-weight:700;display:flex;align-items:center;gap:5px}
.lang i{border:3px solid transparent;border-top:3.5px solid var(--white);margin-top:3px}
.hero-title{left:64px;top:138px;font-family:"Montserrat",sans-serif;font-weight:700;font-size:38px;line-height:47px;color:var(--white)}
.hero-device{left:405px;top:105px;width:285px;height:200px;border-radius:12px;background:linear-gradient(160deg,#1b1f26 0%,#2f353e 40%,#d9e2ea 41%,#f4f6f8 100%);transform:skewY(-14deg) rotate(4deg);box-shadow:0 14px 24px rgba(10,40,80,.35)}

/* about */
.about-title{left:0;width:696px;top:396px;text-align:center;font-family:"Montserrat",sans-serif;font-weight:700;font-size:25px;color:var(--navy)}
.dashes{display:flex;gap:3px}
.dashes span{width:8px;height:4px;border-radius:2px;background:var(--orange)}
.about-dashes{left:375px;top:427px}
.about-lead{left:0;width:696px;top:453px;text-align:center;font-size:8.5px;font-weight:700;color:var(--ink)}
.about-copy{left:113px;width:470px;top:480px;text-align:center;font-size:8px;line-height:20px;color:var(--grey)}

/* services */
.services{left:0;top:614px;width:696px;height:332px;background:linear-gradient(180deg,#0c3d78 0%,#1b66a8 55%,#2a8ac9 100%)}
.card{top:58px;width:262px;height:106px;background:linear-gradient(180deg,var(--coral) 0%,var(--orange) 100%);color:var(--white);text-align:center;padding-top:16px}
.card h3{font-size:9.5px;font-weight:700;margin-bottom:7px}
.card p{font-size:8px;line-height:17.5px;padding:0 24px}
.card-left{left:65px}
.card-right{left:372px}
.tree{left:0;top:164px}
.service{width:72px;text-align:center;color:var(--white);font-size:7.5px;font-weight:700;line-height:11.5px;text-transform:uppercase}
.service svg{display:block;margin:0 auto 5px}

/* newsletter + footer */
.lower{left:0;top:946px;width:696px;height:235px;background:var(--paper)}
.news-label{left:104px;top:994px;font-family:"Lato",sans-serif;font-size:12px;font-weight:500;color:var(--ink)}
.news-form{left:279px;top:987px;width:317px;height:30px;background:var(--white);display:flex;align-items:center}
.news-form .field{flex:1;display:flex;align-items:center;gap:10px;padding-left:14px;font-size:8.5px;color:var(--grey)}
.news-form .btn{width:81px;height:26px;margin-right:2px;background:var(--navy);color:var(--white);font-family:"Roboto",sans-serif;font-weight:700;font-size:9.5px;display:flex;align-items:center;justify-content:center}
.footer-brand{left:66px;top:1047px;font-size:23px}
.footer-about{left:66px;top:1084px;width:181px;font-size:8.5px;line-height:15px;color:var(--grey);text-align:justify}
.socials{left:66px;top:1138px;display:flex;gap:3.5px}
.socials span{width:20px;height:20px;border:1.3px solid var(--navy);border-radius:50%}
.foot-head{top:1047px;font-size:8.5px;font-weight:700;text-decoration:underline;color:var(--ink)}
.contact-row{left:273px;display:flex;align-items:center;gap:13px;font-size:8.5px;line-height:15px;color:var(--grey)}
.contact-row .ring{width:18px;height:18px;border:1.3px solid var(--navy);border-radius:50%;display:flex;align-items:center;justify-content:center;flex:none}
.contact-row .phone{font-size:12.5px;color:var(--grey)}
.links{top:1068px;list-style:none;font-size:8.5px;line-height:18.6px;color:var(--grey)}
.links li::before{content:"»";color:var(--navy);margin-right:9px;font-weight:700}
.bottom-bar{left:0;top:1181px;width:696px;height:19px;background:var(--navy);color:var(--white);font-family:"Roboto",sans-serif;font-size:9px;display:flex;align-items:center;justify-content:center}
</style>
</head>
<body>

<header class="abs hero">
  <div class="abs brand">Tellvik<span class="dot"></span></div>
  <div class="abs hero-mail">
    <span class="ring"><svg width="9" height="7" viewBox="0 0 9 7"><rect x=".5" y=".5" width="8" height="6" rx="1" fill="none" stroke="#fff"/><path d="M.8 1l3.7 2.8L8.2 1" fill="none" stroke="#fff"/></svg></span>
    media@tlv-demo.no
  </div>
  <div class="abs lang">ENG <i></i></div>
  <h1 class="abs hero-title">Page is Under<br>Construction</h1>
  <div class="abs hero-device" role="img" aria-label="Tablet showing a business dashboard with key figures, bar charts and a map"></div>
</header>

<section>
  <h2 class="abs about-title">About Us</h2>
  <div class="abs dashes about-dashes"><span></span><span></span><span></span></div>
  <p class="abs about-lead">DIGITAL SOLUTIONS AND DATA-DRIVEN BUSINESS DEVELOPMENT THAT CREATE VALUE.</p>
  <p class="abs about-copy">TLV Consulting is a consulting company with cutting-edge expertise in digitalisation and data-driven business development. We have extensive experience in data warehouse development, data analysis and reporting, EPM and planning solutions, budget and forecasting solutions for financial and financial data. In short, we help our customers exploit the potential in the available data.</p>
</section>

<section class="abs services">
  <div class="abs card card-left">
    <h3>TELLVIK FOCUS</h3>
    <p>TLV will be the country's leading supplier and competence house on Tellvik software and digital solutions for business management.</p>
  </div>
  <div class="abs card card-right">
    <h3>TELLVIK CONSULTING</h3>
    <p>At TLV Focus, we are passionate about developing good solutions that support the customer's digital strategy. We specialize in providing consulting services.</p>
  </div>
  <svg class="abs tree" width="696" height="60" viewBox="0 0 696 60" fill="none" stroke="rgba(255,255,255,.6)" stroke-width=".8">
    <path d="M196 0V33M81 33H311M81 33V60M158 33V60M234 33V60M311 33V60"/>
    <path d="M503 0V33M388 33H618M388 33V60M465 33V60M541 33V60M618 33V60"/>
  </svg>

  <div class="abs service" style="left:46px;top:228px"><svg width="22" height="22" viewBox="0 0 22 22" fill="none" stroke="#fff" stroke-width="1.1"><rect x="2" y="2" width="6" height="5"/><rect x="14" y="2" width="6" height="5"/><rect x="2" y="15" width="6" height="5"/><rect x="14" y="15" width="6" height="5"/><path d="M5 7v8M17 7v8M8 4h6M8 18h6"/></svg>DATA<br>VAREHUS</div>
  <div class="abs service" style="left:122px;top:228px"><svg width="22" height="22" viewBox="0 0 22 22" fill="none" stroke="#fff" stroke-width="1.1"><rect x="3" y="2" width="16" height="15"/><circle cx="11" cy="10" r="3"/><path d="M3 6h16M7 20h8M11 17v3"/></svg>DATA<br>VISUALISERING</div>
  <div class="abs service" style="left:198px;top:228px"><svg width="22" height="22" viewBox="0 0 22 22" fill="none" stroke="#fff" stroke-width="1.1"><rect x="2" y="2" width="16" height="14"/><circle cx="14" cy="14" r="4"/><path d="M17 17l3 3M5 12V9M8 12V7M11 12V8"/></svg>INTEGRAS<br>JONER</div>
  <div class="abs service" style="left:275px;top:228px"><svg width="22" height="22" viewBox="0 0 22 22" fill="none" stroke="#fff" stroke-width="1.1"><circle cx="8" cy="14" r="5"/><circle cx="8" cy="14" r="2"/><circle cx="16" cy="16" r="3"/><path d="M3 7l5-4 4 3 6-4M18 2h2v2"/></svg>MASKIN<br>LEARING</div>
  <div class="abs service" style="left:353px;top:228px"><svg width="22" height="22" viewBox="0 0 22 22" fill="none" stroke="#fff" stroke-width="1.1"><rect x="2" y="3" width="15" height="13"/><path d="M5 13V9M8 13V7M11 13V10M9 16v4M6 20h6"/><circle cx="16" cy="12" r="3.5"/><path d="M18.5 14.5l2.5 2.5"/></svg>BUSINESS<br>INTELLIGENCE</div>
  <div class="abs service" style="left:429px;top:228px"><svg width="22" height="22" viewBox="0 0 22 22" fill="none" stroke="#fff" stroke-width="1.1"><circle cx="7" cy="15" r="4"/><path d="M7 13v4M3 5l5-2M16 3a2 2 0 110 4 2 2 0 010-4zM14 9h4v5h-1v6h-2v-6h-1z"/></svg>CONSOLIDATION</div>
  <div class="abs service" style="left:507px;top:228px"><svg width="22" height="22" viewBox="0 0 22 22" fill="none" stroke="#fff" stroke-width="1.1"><circle cx="11" cy="5" r="3"/><rect x="3" y="11" width="16" height="9"/><path d="M3 14h16M5 8h3M14 8h3"/></svg>PLANNING</div>
  <div class="abs service" style="left:582px;top:228px"><svg width="22" height="22" viewBox="0 0 22 22" fill="none" stroke="#fff" stroke-width="1.1"><rect x="3" y="2" width="16" height="12"/><circle cx="11" cy="15" r="3"/><path d="M5 21c1-3 3-4 6-4s5 1 6 4"/></svg>CUSTOMER<br>SOLUTION</div>
</section>

<footer>
  <div class="abs lower"></div>
  <p class="abs news-label">SIGN UP FOR NEWSLETTER</p>
  <form class="abs news-form">
    <div class="field"><svg width="10" height="8" viewBox="0 0 10 8"><rect x=".5" y=".5" width="9" height="7" rx="1" fill="none" stroke="#555b63"/><path d="M.8 1l4.2 3 4.2-3" fill="none" stroke="#555b63"/></svg>Enter Your Email</div>
    <div class="btn">SUBSCRIBE</div>
  </form>

  <div class="abs brand footer-brand">Tellvik<span class="dot"></span></div>
  <p class="abs footer-about">Ut enim ad minima veniam, quis nostrum exercitationem ulla corporis suscipit laboriosam, nisi ut aliquid.</p>
  <div class="abs socials" aria-label="Social media"><span></span><span></span><span></span><span></span></div>

  <p class="abs foot-head" style="left:274px">CONTACT US</p>
  <div class="abs contact-row" style="top:1071px">
    <span class="ring"><svg width="8" height="10" viewBox="0 0 8 10"><path d="M4 9.5S1 6 1 4a3 3 0 016 0c0 2-3 5.5-3 5.5z" fill="none" stroke="#0c3468"/><circle cx="4" cy="4" r="1" fill="#0c3468"/></svg></span>
    <span>335 Lorem ipsum dolor<br>United States</span>
  </div>
  <div class="abs contact-row" style="top:1108px">
    <span class="ring"><svg width="9" height="7" viewBox="0 0 9 7"><rect x=".5" y=".5" width="8" height="6" rx="1" fill="none" stroke="#0c3468"/><path d="M.8 1l3.7 2.8L8.2 1" fill="none" stroke="#0c3468"/></svg></span>
    <span>media@tlv-demo.no</span>
  </div>
  <div class="abs contact-row" style="top:1139px">
    <span class="ring"><svg width="9" height="9" viewBox="0 0 9 9"><path d="M2 1l1.5 2-1 1c.6 1.3 1.3 2 2.5 2.5l1-1L8 7l-1 1.3C4 8 1 5 .8 2z" fill="none" stroke="#0c3468"/></svg></span>
    <span class="phone">888 888 8889</span>
  </div>

  <p class="abs foot-head" style="left:454px">QUICK LINKS</p>
  <ul class="abs links" style="left:454px">
    <li>Home</li><li>About Us</li><li>Our Vision</li><li>Resources</li><li>Reviews</li>
  </ul>
  <p class="abs foot-head" style="left:554px">OTHER LINKS</p>
  <ul class="abs links" style="left:554px">
    <li>Contact Us</li><li>FAQ</li><li>Help Service</li><li>Terms Of Use</li><li>Privacy Policy</li>
  </ul>

  <div class="abs bottom-bar">© 2020 Tellvik. All Rights Reserved</div>
</footer>

</body>
</html>
```